Web Design job - Condo Debts Collection Business needs a Web Design

I need a site for a client, who works with condo debts collection, and ensure all revenues provided by condo fees will be always available to the building manager of condo on a specific date, regardless of defaults.
I have the visual identity (logo, slogan and colors) of the company, and some requirements on layout (kind of slider, menu options, phone number on a noble position, etc) - maybe I can do a sketch, but I like the idea of give some freedom to designer.

*** PLEASE, we have no interest in templates. We want something new***

Target Market(s)

I have two targets for this design: - Condominium's building manager. This target is looking for a solution to overdue debts on it's condo. - Residents on condominiums. This target wants to live in a better place, where their neighbors pay their condominium fees on time.

Number of Pages Required

1 page

Requirements
Must have
• - Slider with title, some short text related, a nice image (I prefer happy and/or peaceful family, people doing business, happy friends, and so on).
• - I have a special attention to menu. I'm looking for one I can have a nice effect, more elegant, charming, kind of innovative.
• - Phone number on the top (or clearly visible).
• - Member log in area or icon on the top (or clearly visible).
• - News/articles area.
• - Modern fonts, with good quality, sans-serif on areas where reading is more intensive (prefer Google web-fonts).
• - Colors specified on attached files.
Nice to have
• - Clear background color, cause it's better to read larger texts (like articles). Dark backgrounds makes reading difficult.
• - A site with effects (like shadows, lines, curves, gradients, lights) is usually pretty.
• - I pay attention on beautiful footers.
Should not have
• - Images with a lot of money (I don't sell richness, I sell tranquility, peace, harmony, safety).
• - Poor menu.

```html
<!DOCTYPE html>
<html lang="en">
<head>
<meta charset="utf-8">
<title>Novara — Condominium Revenue Assurance</title>
<link rel="stylesheet" href="https://fonts.googleapis.com/css2?family=Cinzel:wght@400;700&family=Arimo:wght@400;700&display=swap">
<style>
:root{
  --gold:#e8b422;
  --gold-dark:#c9951a;
  --ink:#2b2b2b;
  --text:#333;
  --muted:#888;
  --paper:#ffffff;
  --mist:#f1f3f6;
  --night:#24242a;
  --night-soft:#3a3a42;
}
*{margin:0;padding:0;box-sizing:border-box}
html,body{width:1200px;height:3093px;overflow:hidden}
body{position:relative;background:var(--paper);font-family:"Arimo",Arial,sans-serif;color:var(--text);font-size:12.5px;line-height:19px}
.abs{position:absolute}
.serif{font-family:"Cinzel",Georgia,serif;font-weight:400;text-transform:uppercase;letter-spacing:1px}
.gold{color:var(--gold)}
.btn{display:inline-block;background:var(--gold);color:#fff;font-size:11px;font-weight:700;text-transform:uppercase;text-align:center;letter-spacing:.5px}
.photo{position:absolute}
.section-title{font-family:"Cinzel",Georgia,serif;font-weight:400;font-size:25px;letter-spacing:1px;color:var(--ink);text-transform:uppercase;padding-left:18px;border-left:3px solid var(--gold);line-height:26px;white-space:nowrap}
.section-title span{color:var(--gold)}
.sub-title{font-family:"Cinzel",Georgia,serif;font-weight:400;font-size:19px;color:var(--ink);text-transform:uppercase;margin:22px 0 6px}
.sub-title span{color:var(--gold)}

/* header */
.brand{left:233px;top:12px;font-family:"Arimo",sans-serif;font-weight:700;font-size:28px;color:var(--ink);display:flex;align-items:center;gap:8px}
.brand i{width:22px;height:22px;background:var(--gold);display:block}
.nav{top:24px;font-size:10px;line-height:12px;text-transform:uppercase;color:var(--ink);white-space:nowrap}
.nav .active{color:var(--gold);border-bottom:1px solid var(--gold);padding-bottom:2px}
.login{left:783px;top:17px;width:76px;height:27px;line-height:27px}
.phone{left:866px;top:17px;width:100px;height:27px;line-height:27px;display:flex;align-items:center;justify-content:center;gap:5px;font-size:10.5px;letter-spacing:0}

/* hero */
.hero-title{left:566px;top:154px;font-size:30px;line-height:37px;color:var(--ink);border-left:3px solid var(--gold);padding-left:18px;width:430px}
.hero-text{left:587px;top:234px;width:360px;font-size:11.5px;line-height:18px}
.hero-btn{left:587px;top:288px;width:122px;height:33px;line-height:33px}

/* welcome */
.welcome{left:233px;top:560px;width:380px}
.welcome p{font-size:12px;line-height:18px;margin-left:21px}
.welcome .sub-title{margin-left:21px}
.welcome .btn{margin:30px 0 0 21px;width:122px;height:33px;line-height:33px}

/* cards */
.card{position:absolute;background:#fff;box-shadow:0 4px 14px rgba(0,0,0,.12)}
.card .card-body{padding:14px 16px 14px 20px}
.card h3{font-family:"Cinzel",Georgia,serif;font-weight:400;font-size:16px;color:var(--ink);text-transform:uppercase;margin-bottom:6px}
.card h3 span{color:var(--gold)}
.card p{font-size:11px;line-height:17px}
.card a{display:inline-block;margin-top:6px;font-family:"Cinzel",Georgia,serif;font-size:10px;color:var(--gold);text-decoration:underline}
.date{position:absolute;right:6px;top:0;width:30px;height:34px;background:var(--gold);color:#fff;font-size:13px;line-height:14px;text-align:center;padding-top:4px;font-weight:700}
.date small{display:block;font-size:8px;font-weight:400}

/* testimonial */
.quote-card{left:355px;top:2213px;width:490px;height:158px;background:#fff;box-shadow:0 6px 16px rgba(0,0,0,.15);text-align:center;padding:48px 60px 0}
.quote-card p{font-size:12px;line-height:18px}
.quote-card .who{margin-top:8px;font-family:"Cinzel",Georgia,serif;font-size:11px;color:var(--ink)}
.stack{background:#fff;box-shadow:0 3px 6px rgba(0,0,0,.12)}
.arrow{width:26px;height:26px;border:1px solid var(--gold);border-radius:50%;display:flex;align-items:center;justify-content:center}

/* newsletter */
.news-input{left:557px;top:2604px;width:233px;height:31px;border:1px solid #e5e5e5;font-size:11px;color:var(--muted);line-height:29px;padding-left:12px}
.news-btn{left:790px;top:2604px;width:92px;height:31px;line-height:31px}

/* footer */
.foot-col h4{font-family:"Cinzel",Georgia,serif;font-weight:400;font-size:13px;color:var(--gold);text-transform:uppercase;border-left:2px solid var(--gold);padding-left:14px;margin-bottom:14px}
.foot-col li{list-style:none;color:#9a9aa2;font-size:10.5px;line-height:21px;padding-left:16px}
.contact li{display:flex;gap:8px;align-items:flex-start}
.contact svg{flex:none;margin-top:5px}
.copyright{left:0;top:3052px;width:1200px;text-align:center;font-size:10px;color:#8d8d95}
</style>
</head>
<body>

<svg class="abs" style="left:0;top:0" width="1200" height="620" aria-hidden="true">
  <rect width="1200" height="620" fill="var(--mist)"/>
  <polygon points="0,528 780,418 0,546" fill="var(--gold)"/>
  <polygon points="0,546 780,418 1200,370 1200,620 0,620" fill="#fff"/>
</svg>
<div class="photo" role="img" aria-label="Photo of three cheerful colleagues raising their arms in celebration" style="left:50px;top:0;width:517px;height:520px;background:linear-gradient(160deg,#e6e8ea 0%,#c7ccd2 45%,#6d7078 100%);clip-path:polygon(0 0,100% 0,100% 82%,0 100%)"></div>

<header>
  <div class="abs brand"><i></i>Novara</div>
  <nav>
    <span class="abs nav active" style="left:482px">Home</span>
    <span class="abs nav" style="left:527px">About Us</span>
    <span class="abs nav" style="left:589px">Services</span>
    <span class="abs nav" style="left:651px">News</span>
    <span class="abs nav" style="left:697px">Get in touch</span>
  </nav>
  <div class="abs btn login">&#9679; Log in</div>
  <div class="abs btn phone">
    <svg width="10" height="10" viewBox="0 0 24 24"><path fill="#fff" d="M6.6 10.8a15 15 0 006.6 6.6l2.2-2.2c.3-.3.7-.4 1-.2 1.1.4 2.3.6 3.6.6.6 0 1 .4 1 1V20c0 .6-.4 1-1 1A17 17 0 013 4c0-.6.4-1 1-1h3.5c.6 0 1 .4 1 1 0 1.3.2 2.5.6 3.6.1.3 0 .7-.2 1z"/></svg>
    (55) 3100.2040
  </div>
</header>

<section>
  <h1 class="abs hero-title serif">Lorem ipsum dolor sit amet, <span class="gold">consectetur</span></h1>
  <p class="abs hero-text">Lorem ipsum dolor sit amet, consectetur adipiscing elit. Aliquam<br>ut dignissim dolor. Pellentesque ex elit, interdum at ex.</p>
  <div class="abs btn hero-btn">Get in touch</div>
</section>

<section>
  <div class="abs welcome">
    <h2 class="section-title"><span>Welcome</span> to Novara</h2>
    <p style="margin-top:20px">Mauris non faucibus felis. Nunc feugiat condimentum nulla, in tincidunt neque suscipit sed. Etiam ac finibus velit. Curabitur vulputate nunc et facilisis malesuada. Praesent id odio mi. Sed tempor orci a bibendum vehicula. Quisque eget enim non est viverra iaculis.</p>
    <h3 class="sub-title"><span>Our</span> Vision</h3>
    <p>Nulla gravida ante sit amet nibh imperdiet viverra. Etiam lectus dolor, sodales sit amet velit ut, ornare vulputate purus. Senectus et netus et malesuada fames ac turpis egestas.</p>
    <h3 class="sub-title"><span>Our</span> Mission</h3>
    <p>Etiam lectus dolor, sodales sit amet velit ut, ornare vulputate purus. Nulla eget laoreet felis. Pellentesque habitant morbi tristique senectus et netus et malesuada fames ac turpis egestas.</p>
    <div class="btn">Learn more</div>
  </div>
  <svg class="abs" style="left:677px;top:520px" width="180" height="432" aria-hidden="true">
    <rect x="0" y="0" width="8" height="432" fill="var(--gold)"/>
    <polygon points="0,420 176,420 176,432 0,432" fill="var(--gold)"/>
  </svg>
  <div class="photo" role="img" aria-label="Photo of hands reviewing house plans beside a small model home" style="left:690px;top:532px;width:510px;height:406px;background:linear-gradient(135deg,#f3f3f1 0%,#dfe1e3 50%,#b9bec4 100%)"></div>
</section>

<svg class="abs" style="left:0;top:990px" width="1200" height="700" aria-hidden="true">
  <defs><linearGradient id="svcbg" x1="0" y1="0" x2="0" y2="1"><stop offset="0" stop-color="#f4f6f8"/><stop offset="1" stop-color="#e1e6ec"/></linearGradient></defs>
  <polygon points="0,160 1200,10 1200,618 0,660" fill="url(#svcbg)"/>
  <polygon points="310,150 1200,0 1200,24" fill="var(--gold)"/>
  <polygon points="0,660 1200,548 1200,560 0,684" fill="var(--gold)"/>
  <polygon points="0,684 1200,560 1200,700 0,700" fill="#fff"/>
</svg>

<section>
  <div class="abs" style="left:233px;top:1197px;width:300px">
    <h2 class="section-title"><span>Our</span> Services</h2>
    <p style="margin:20px 0 0 21px;font-size:12px;line-height:18px">Etiam ac finibus velit. Curabitur vulputate nunc et facilisis malesuada. Praesent id odio mi. Sed tempor orci a bibendum vehicula.</p>
    <div class="btn" style="margin:22px 0 0 21px;width:122px;height:33px;line-height:33px">View more</div>
  </div>
  <article class="card" style="left:546px;top:1204px;width:198px;height:250px">
    <div role="img" aria-label="Photo of a business handshake across a desk" style="height:103px;background:linear-gradient(135deg,#8a8f96,#3d4047)"></div>
    <div class="card-body"><h3><span>Service</span> One</h3><p>Etiam ac finibus velit. Curabitur arvulputate nunc et facilisis malesuada praesent id odiomi.</p><a>Learn more</a></div>
  </article>
  <article class="card" style="left:767px;top:1204px;width:198px;height:250px">
    <div role="img" aria-label="Photo of a person signing documents with a pen" style="height:103px;background:linear-gradient(135deg,#a58a6e,#4a3a2e)"></div>
    <div class="card-body"><h3><span>Service</span> Two</h3><p>Etiam ac finibus velit. Curabitur arvulputate nunc et facilisis malesuada praesent id odiomi.</p><a>Learn more</a></div>
  </article>
</section>

<section>
  <article class="card" style="left:233px;top:1695px;width:200px;height:247px">
    <div role="img" aria-label="Photo of a residential condominium building" style="position:relative;height:105px;background:linear-gradient(180deg,#4d8fd6 0%,#9bc2ea 45%,#b99c84 100%)"></div>
    <div class="date">13<small>JUL</small></div>
    <div class="card-body"><h3>News Headline</h3><p>Etiam ac finibus velit. Curabitu arvulputate nunc et facilisis malesuada praesent id odiomi.</p><a>Read more</a></div>
  </article>
  <article class="card" style="left:456px;top:1695px;width:198px;height:247px">
    <div role="img" aria-label="Photo of a modern apartment block with trees" style="position:relative;height:105px;background:linear-gradient(180deg,#5a9ad8 0%,#a3a9ad 50%,#5f8a44 100%)"></div>
    <div class="date">13<small>JUL</small></div>
    <div class="card-body"><h3>News Headline2</h3><p>Etiam ac finibus velit. Curabitu arvulputate nunc et facilisis malesuada praesent id odiomi.</p><a>Read more</a></div>
  </article>
  <div class="abs" style="left:683px;top:1692px;width:290px">
    <h2 class="section-title"><span>Latest</span> News</h2>
    <p style="margin:20px 0 0 21px;font-size:12px;line-height:18px">Etiam ac finibus velit. Curabitur <span style="color:var(--muted)">vulputate nunc et facilisis malesuada. Praesent</span> id odio mi. <span style="color:var(--muted)">Sed tempor orci a bibendum vehicula.</span></p>
    <div class="btn" style="margin:22px 0 0 21px;width:122px;height:33px;line-height:33px">Read more</div>
  </div>
</section>

<svg class="abs" style="left:0;top:1920px" width="1200" height="680" aria-hidden="true">
  <polygon points="0,170 1200,8 1200,30 0,190" fill="var(--gold-dark)" opacity=".6"/>
</svg>
<div class="photo" role="img" aria-label="Golden-toned photo of an apartment building facade with trees" style="left:0;top:1928px;width:1200px;height:650px;background:linear-gradient(120deg,#d9a425 0%,#e6b73a 40%,#c99a2c 75%,#a8842f 100%);clip-path:polygon(0 24%,100% 0,100% 79%,0 100%)"></div>
<section>
  <h2 class="abs serif" style="left:0;top:2098px;width:1200px;text-align:center;color:#fff;font-size:23px">What our client speak</h2>
  <p class="abs" style="left:390px;top:2142px;width:420px;text-align:center;color:#fff;font-size:12px;line-height:18px">Etiam ac finibus velit. Curabitur vulputate nunc et facilisis malesuada. Praesent id odio mi. Sed tempor orci a bibendum vehicula.</p>
  <div class="abs stack" style="left:375px;top:2381px;width:450px;height:10px"></div>
  <div class="abs stack" style="left:365px;top:2373px;width:470px;height:10px"></div>
  <div class="abs quote-card">
    <p>Mauris non faucibus felis. Nunc feugiat condimentum nulla, in tincidunt neque suscipit sed. Etiam ac finibus velit. Curabitur vulputate nunc et facilisis malesuada. Praesent id odio mi sed tempor orcia.</p>
    <div class="who"><span class="gold">Mark Ellis</span> (Lorem Ipsum Co.)</div>
  </div>
  <svg class="abs" style="left:578px;top:2194px" width="44" height="44" aria-hidden="true">
    <circle cx="22" cy="22" r="21" fill="#e9e9e9"/>
    <text x="22" y="38" text-anchor="middle" font-family="Georgia,serif" font-size="34" fill="#fff">&#8220;</text>
  </svg>
  <div class="abs arrow" style="left:376px;top:2278px"><svg width="8" height="10"><path d="M7 1L2 5l5 4" stroke="var(--gold)" fill="none" stroke-width="1.5"/></svg></div>
  <div class="abs arrow" style="left:796px;top:2278px"><svg width="8" height="10"><path d="M1 1l5 4-5 4" stroke="var(--gold)" fill="none" stroke-width="1.5"/></svg></div>
</section>

<section>
  <div class="abs" style="left:233px;top:2598px;width:320px">
    <h2 class="section-title"><span>Newsletter</span> Signup</h2>
    <p style="margin:8px 0 0 21px;font-size:12px;line-height:18px">Sign up our newsletter to get more updates about our services rgarding condo, building or property.</p>
  </div>
  <div class="abs news-input">Your Email Address</div>
  <div class="abs btn news-btn">Sign up</div>
</section>

<svg class="abs" style="left:0;top:2670px" width="1200" height="423" aria-hidden="true">
  <polygon points="0,92 1200,10 1200,24 0,106" fill="var(--gold)"/>
  <polygon points="0,165 1200,24 1200,423 0,423" fill="var(--night)"/>
</svg>
<footer>
  <div class="abs" style="left:233px;top:2852px;width:200px">
    <div style="display:flex;align-items:center;gap:8px;font-weight:700;font-size:26px;color:#fff"><i style="width:20px;height:20px;background:var(--gold);display:block"></i>Novara</div>
    <p style="margin-top:12px;font-size:10px;line-height:15px;color:#9a9aa2">Mauris non faucibus felis. Nunc feugiat condimentum nulla.</p>
    <div style="display:flex;gap:16px;margin-top:16px">
      <i style="width:7px;height:7px;background:var(--gold);display:block"></i>
      <i style="width:7px;height:7px;background:var(--gold);display:block"></i>
      <i style="width:7px;height:7px;background:var(--gold);display:block"></i>
      <i style="width:7px;height:7px;background:var(--gold);display:block"></i>
    </div>
  </div>
  <div class="abs foot-col" style="left:455px;top:2854px">
    <h4>About Us</h4>
    <ul><li>Who We Are</li><li>News</li><li>Our Partners</li></ul>
  </div>
  <div class="abs foot-col contact" style="left:597px;top:2854px;width:240px">
    <h4>Contact Us</h4>
    <ul>
      <li><svg width="9" height="9" viewBox="0 0 24 24"><path fill="var(--gold)" d="M6.6 10.8a15 15 0 006.6 6.6l2.2-2.2c.3-.3.7-.4 1-.2 1.1.4 2.3.6 3.6.6.6 0 1 .4 1 1V20c0 .6-.4 1-1 1A17 17 0 013 4c0-.6.4-1 1-1h3.5c.6 0 1 .4 1 1 0 1.3.2 2.5.6 3.6.1.3 0 .7-.2 1z"/></svg>(55) 3100.2040</li>
      <li><svg width="10" height="8" viewBox="0 0 20 14"><rect x="1" y="1" width="18" height="12" fill="none" stroke="var(--gold)" stroke-width="2"/><path d="M1 1l9 7 9-7" fill="none" stroke="var(--gold)" stroke-width="2"/></svg>hello@novara.example</li>
      <li style="line-height:16px;padding-top:3px"><svg width="8" height="11" viewBox="0 0 16 22"><path fill="var(--gold)" d="M8 0a8 8 0 018 8c0 6-8 14-8 14S0 14 0 8a8 8 0 018-8zm0 5a3 3 0 100 6 3 3 0 000-6z"/></svg><span>Rua das Palmeiras 480, Suite 705,<br>Palm Court Tower, Centro,<br>Vila Serena, 60100-000</span></li>
    </ul>
  </div>
  <div class="abs foot-col" style="left:858px;top:2854px">
    <h4>Our Services</h4>
    <ul><li>Service one</li><li>Service two</li><li>Service three</li></ul>
  </div>
  <div class="abs" style="left:233px;top:3030px;width:734px;height:1px;background:var(--night-soft)"></div>
  <p class="abs copyright">© 2019 novara.example . All rights reserved. Privacy Policy | Legal Statement | Website map</p>
</footer>

</body>
</html>
```